Plumwave business card

We need a modern business card - With our 4 colors - See web: www.plumwave.dk

I have attached logo and som old business Cards we have - Lets Make the new ones shine...:-) -

Industry/Entity Type

Business

Requirements
Must have
• the logo with plumwave only,

```html
<!DOCTYPE html>
<html lang="da">
<head>
<meta charset="utf-8">
<title>Plumwave – visitkort</title>
<link rel="stylesheet" href="https://fonts.googleapis.com/css2?family=PT+Sans:wght@400;700&display=swap">
<style>
  :root {
    --page: #d9d6d1;
    --card: #f1f2ef;
    --green-dark: #3d8a27;
    --green-light: #72b446;
    --band: #1f1f1f;
    --ink: #2b2b2b;
    --on-green: #f4e9e3;
    --rule: #6cae3f;
  }
  * { margin: 0; padding: 0; box-sizing: border-box; }
  html, body {
    width: 1200px; height: 969px; overflow: hidden;
    background: var(--page);
    font-family: "PT Sans", Arial, sans-serif;
  }
  .card {
    position: absolute; left: 100px; top: 200px;
    width: 1000px; height: 569px;
    border-radius: 24px; overflow: hidden;
    background: var(--card);
    box-shadow: 0 10px 30px rgba(0,0,0,0.18);
  }
  .card-wave { position: absolute; inset: 0; width: 100%; height: 100%; }
  .brand { position: absolute; left: 48px; top: 70px; width: 366px; text-align: center; }
  .brand-dot {
    display: block; width: 90px; height: 90px; margin: 0 auto 14px;
    border-radius: 50%; background: var(--green-light);
  }
  .brand-name { font-size: 32px; letter-spacing: 2px; color: var(--ink); line-height: 1; }
  .brand-rule { height: 3px; background: var(--rule); margin-top: 16px; }
  .brand-tagline { margin-top: 14px; font-size: 22px; font-weight: 700; color: var(--ink); }
  .contact { position: absolute; right: 60px; top: 206px; text-align: right; color: var(--on-green); }
  .contact-name { font-size: 36px; line-height: 44px; }
  .contact-title { font-size: 24px; line-height: 32px; margin-bottom: 14px; }
  .contact-line {
    display: flex; justify-content: flex-end; align-items: center;
    font-size: 24px; line-height: 41px; gap: 18px;
  }
  .contact-icon { width: 22px; height: 22px; fill: var(--on-green); }
  .contact-address { font-size: 24px; line-height: 41px; }
</style>
</head>
<body>
  <div class="card">
    <svg class="card-wave" viewBox="0 0 580 330" preserveAspectRatio="none" aria-hidden="true">
      <defs>
        <linearGradient id="greenFill" x1="0" y1="1" x2="1" y2="0">
          <stop offset="0" stop-color="var(--green-light)"/>
          <stop offset="1" stop-color="var(--green-dark)"/>
        </linearGradient>
      </defs>
      <path d="M0,212 C60,250 130,292 220,262 C330,222 420,72 580,57 L580,330 L0,330 Z" fill="url(#greenFill)"/>
      <path d="M0,204 C60,244 130,284 220,254 C330,214 420,64 580,49" fill="none" stroke="var(--band)" stroke-width="7"/>
    </svg>

    <div class="brand">
      <span class="brand-dot"></span>
      <div class="brand-name">plumwave</div>
      <div class="brand-rule"></div>
      <div class="brand-tagline">medier til unge</div>
    </div>

    <div class="contact">
      <div class="contact-name">Maren Holstvig</div>
      <div class="contact-title">Salgsdirektør</div>
      <div class="contact-line">+45 31 42 60 18
        <svg class="contact-icon" viewBox="0 0 24 24"><path d="M6.6 10.8a15.1 15.1 0 0 0 6.6 6.6l2.2-2.2a1 1 0 0 1 1-.25 11.4 11.4 0 0 0 3.6.57 1 1 0 0 1 1 1V20a1 1 0 0 1-1 1A17 17 0 0 1 3 4a1 1 0 0 1 1-1h3.5a1 1 0 0 1 1 1c0 1.25.2 2.45.57 3.57a1 1 0 0 1-.25 1z"/></svg>
      </div>
      <div class="contact-line">+45 52 73 19 04
        <svg class="contact-icon" viewBox="0 0 24 24"><path d="M6.6 10.8a15.1 15.1 0 0 0 6.6 6.6l2.2-2.2a1 1 0 0 1 1-.25 11.4 11.4 0 0 0 3.6.57 1 1 0 0 1 1 1V20a1 1 0 0 1-1 1A17 17 0 0 1 3 4a1 1 0 0 1 1-1h3.5a1 1 0 0 1 1 1c0 1.25.2 2.45.57 3.57a1 1 0 0 1-.25 1z"/></svg>
      </div>
      <div class="contact-line">mh@plumwave.dk
        <svg class="contact-icon" viewBox="0 0 24 24"><path d="M3 5h18v14H3z M3 5l9 7 9-7" fill="none" stroke="var(--on-green)" stroke-width="2"/></svg>
      </div>
      <div class="contact-line">www.plumwave.dk
        <svg class="contact-icon" viewBox="0 0 24 24"><circle cx="12" cy="12" r="9" fill="none" stroke="var(--on-green)" stroke-width="2"/><path d="M3 12h18M12 3c3 3 3 15 0 18M12 3c-3 3-3 15 0 18" fill="none" stroke="var(--on-green)" stroke-width="1.6"/></svg>
      </div>
      <div class="contact-address">Kastanjevej 12, 2000 Frederiksberg</div>
    </div>
  </div>
</body>
</html>
```